Business Card for Mortuary

We need a business card design for our mortuary. We are not the "traditional" mortuary and specialize in simple cremations and burials. We use a two sided card.

Industry/Entity Type

Funeral Home

Contact Information for Business Card

One side we would like to have with the general information of the mortuary:
Address: 4127 E. Larkspur Ave, Sun City, AZ 85399
Phone: 623-555-0142
email: hello@willowbendmortuary.example
website: willowbendmortuary.example

On the other side would like to have the information of employee:
Name: Mark T. Ellis
Email: mark@willowbendmortuary.example
Title: Funeral Director
Text: 602-555-0187

Font styles to use
Serif
Sans Serif

Requirements
Should not have
• Do not put any gothic images or things like a hearse or tombstone.

```html
<!DOCTYPE html>
<html lang="en">
<head>
<meta charset="utf-8">
<title>Willowbend Mortuary – Business Cards</title>
<link href="https://fonts.googleapis.com/css2?family=Arimo:wght@400;700&family=Nunito+Sans:wght@400;700;800&display=swap" rel="stylesheet">
<style>
  :root{
    --page:#d4d4d4;
    --paper:#ffffff;
    --ink:#111111;
    --ink-soft:#222222;
    --lime:#8cc63f;
    --lime-bright:#c3dc3a;
    --leaf:#6db33f;
    --forest:#3e6c55;
    --forest-light:#4f8a6c;
    --white:#ffffff;
  }
  *{box-sizing:border-box;margin:0;padding:0}
  html,body{width:1200px;height:800px;overflow:hidden;background:var(--page)}
  body{position:relative;font-family:"Nunito Sans",sans-serif}

  .card{position:absolute;top:284px;width:430px;height:238px;overflow:hidden}
  .card--front{left:110px;background:var(--paper)}
  .card--back{left:638px;background:radial-gradient(ellipse at 40% 35%,var(--forest-light) 0%,var(--forest) 70%)}

  .brand{position:absolute;display:flex;align-items:center;gap:5px}
  .brand__dot{width:34px;height:34px;border-radius:50%;background:var(--lime);flex:none}
  .brand__name{font-family:"Arimo",sans-serif;font-weight:700;font-size:18px;line-height:18px;letter-spacing:-.2px;text-transform:uppercase}
  .brand__rule{width:1px;height:40px;background:var(--lime);margin-left:3px}
  .brand__tagline{font-family:"Arimo",sans-serif;font-size:11.5px;line-height:14px;color:var(--lime)}

  .card--front .brand{left:30px;top:58px}
  .card--front .brand__name{color:var(--ink)}
  .card--back .brand{left:168px;top:58px}
  .card--back .brand__name{color:var(--white)}
  .card--back .brand__tagline{color:var(--white)}

  .motif{position:absolute}
  .card--front .motif{right:0;bottom:0;width:130px;height:190px;
    background:radial-gradient(ellipse at 85% 75%,var(--leaf) 0%,var(--lime) 40%,rgba(195,220,58,.35) 70%,rgba(255,255,255,0) 85%)}
  .card--back .motif{left:0;top:0;width:125px;height:238px;
    background:radial-gradient(ellipse at 20% 50%,var(--lime-bright) 0%,rgba(140,198,63,.75) 45%,rgba(62,108,85,0) 80%)}

  .person{position:absolute;right:170px;top:126px;text-align:right}
  .person__name{font-weight:800;font-size:18px;letter-spacing:1px;color:var(--ink);text-transform:uppercase}
  .person__title{font-size:11.5px;color:var(--lime);margin-top:1px}
  .dash{display:block;width:10px;height:1px;background:var(--lime)}
  .person .dash{margin:12px 0 0 auto}

  .contact{list-style:none;font-size:11px;line-height:14.5px}
  .contact li{display:flex;align-items:center;gap:7px}
  .contact svg{width:11px;height:11px;flex:none}
  .card--front .contact{position:absolute;right:170px;top:195px;color:var(--ink-soft)}
  .card--front .contact li{justify-content:flex-end}

  .office{position:absolute;left:205px;top:132px;color:var(--white)}
  .office__address{font-size:11px;line-height:14px}
  .office .dash{margin:8px 0 8px}
  .office .contact li{gap:7px}
  .web__domain{color:var(--lime-bright)}
</style>
</head>
<body>

<section class="card card--front" aria-label="Business card front">
  <div class="brand">
    <span class="brand__dot"></span>
    <span class="brand__name">Willowbend<br>Mortuary</span>
    <span class="brand__rule"></span>
    <span class="brand__tagline">Affordable<br>Cremation<br>and Burial</span>
  </div>

  <div class="person">
    <p class="person__name">Mark T. Ellis</p>
    <p class="person__title">Funeral Director</p>
    <span class="dash"></span>
  </div>

  <ul class="contact">
    <li>602-555-0187
      <svg viewBox="0 0 12 12" fill="none" stroke="#8cc63f" stroke-width="1"><rect x="1" y="2.5" width="10" height="7"/><path d="M1 2.5l5 4 5-4"/></svg>
    </li>
    <li>mark@willowbendmortuary.example
      <svg viewBox="0 0 12 12" fill="none" stroke="#8cc63f" stroke-width="1"><rect x="1" y="4" width="10" height="7"/><path d="M1 4l5 4 5-4M3 4V1.5h6V4"/></svg>
    </li>
  </ul>

  <div class="motif" role="img" aria-label="Soft green leaf motif in the corner"></div>
</section>

<section class="card card--back" aria-label="Business card back">
  <div class="motif" role="img" aria-label="Large soft green leaf motif along the left edge"></div>

  <div class="brand">
    <span class="brand__dot"></span>
    <span class="brand__name">Willowbend<br>Mortuary</span>
    <span class="brand__rule"></span>
    <span class="brand__tagline">Affordable<br>Cremation<br>and Burial</span>
  </div>

  <div class="office">
    <p class="office__address">4127 E. Larkspur Ave<br>Sun City, AZ 85399</p>
    <span class="dash"></span>
    <ul class="contact">
      <li><svg viewBox="0 0 12 12" fill="none" stroke="#c3dc3a" stroke-width="1"><path d="M2 1.5l2 0 1 2.5-1.3 1a6 6 0 0 0 3.3 3.3l1-1.3 2.5 1v2a1 1 0 0 1-1 1A9 9 0 0 1 1 2.5a1 1 0 0 1 1-1z"/></svg>623-555-0142</li>
      <li><svg viewBox="0 0 12 12" fill="none" stroke="#c3dc3a" stroke-width="1"><rect x="1" y="2.5" width="10" height="7"/><path d="M1 2.5l5 4 5-4"/></svg>hello@willowbendmortuary.example</li>
      <li><svg viewBox="0 0 12 12" fill="none" stroke="#c3dc3a" stroke-width="1"><circle cx="6" cy="6" r="5"/><path d="M1 6h10M6 1c-2.5 3-2.5 7 0 10M6 1c2.5 3 2.5 7 0 10"/></svg><span>www.<span class="web__domain">willowbendmortuary</span>.example</span></li>
    </ul>
  </div>
</section>

</body>
</html>
```